Business card for event manager / organizer "velmora tandem"

Draft of a new valuable business card for my company.
Events, personnel service providers, festivals

```html
<!DOCTYPE html>
<html lang="de">
<head>
<meta charset="utf-8">
<title>velmora tandem – Visitenkarte</title>
<link rel="stylesheet" href="https://fonts.googleapis.com/css2?family=Roboto:wght@300;400;700&display=swap">
<style>
  :root {
    --stage: #2b2b2e;
    --card: #060606;
    --orange: #e8801e;
    --white: #ffffff;
    --muted: #bdbdbd;
    --photo-a: #3a3a3c;
    --photo-b: #101010;
  }
  * { box-sizing: border-box; margin: 0; padding: 0; }
  html, body { width: 1200px; height: 913px; overflow: hidden; }
  body {
    background: var(--stage);
    font-family: "Roboto", Arial, sans-serif;
    color: var(--white);
    position: relative;
  }
  .card {
    position: absolute;
    width: 540px;
    height: 310px;
    background: var(--card);
    border-radius: 14px;
    overflow: hidden;
    box-shadow: 0 10px 30px rgba(0,0,0,.45);
  }
  .card--front { left: 40px; top: 301px; }
  .card--back  { left: 620px; top: 301px; border-bottom: 3px solid var(--orange); }

  /* front */
  .portrait {
    position: absolute; left: 18px; top: 40px; width: 200px; height: 250px;
    background: radial-gradient(ellipse at 50% 35%, var(--photo-a), var(--photo-b) 75%);
  }
  .front-bands { position: absolute; inset: 0; width: 100%; height: 100%; }
  .edge-mark {
    position: absolute; right: 0; top: 34px; width: 7px; height: 30px; background: var(--orange);
  }
  .brand { display: flex; align-items: center; gap: 8px; }
  .brand__mark { background: var(--orange); flex: none; }
  .brand__name { font-weight: 700; color: var(--white); letter-spacing: .5px; white-space: nowrap; }
  .brand--small { position: absolute; right: 40px; top: 26px; }
  .brand--small .brand__mark { width: 26px; height: 26px; }
  .brand--small .brand__name { font-size: 22px; }
  .tagline { font-weight: 300; color: var(--muted); white-space: nowrap; }
  .tagline--small { position: absolute; right: 40px; top: 58px; font-size: 7px; }

  .identity { position: absolute; right: 40px; top: 74px; text-align: right; }
  .identity__name { color: var(--orange); font-size: 20px; font-weight: 400; letter-spacing: .5px; }
  .identity__role { font-size: 11px; letter-spacing: 1px; margin-top: 2px; }

  .contacts { position: absolute; right: 40px; top: 120px; list-style: none; text-align: right; }
  .contacts li { font-size: 11.5px; line-height: 16px; display: flex; justify-content: flex-end; align-items: center; gap: 5px; white-space: nowrap; }
  .contacts svg { width: 9px; height: 9px; fill: none; stroke: var(--orange); stroke-width: 2; flex: none; }

  /* back */
  .brand--large { position: absolute; left: 140px; top: 104px; }
  .brand--large .brand__mark { width: 54px; height: 54px; }
  .brand--large .brand__name { font-size: 38px; }
  .tagline--large { position: absolute; left: 202px; top: 164px; font-size: 11px; }
  .social {
    position: absolute; left: 140px; bottom: 34px; font-size: 14px;
    display: flex; align-items: center; gap: 7px; white-space: nowrap;
  }
  .social__dot { width: 10px; height: 10px; border-radius: 50%; background: var(--orange); flex: none; }
</style>
</head>
<body>

<section class="card card--front" aria-label="Vorderseite">
  <div class="portrait" role="img" aria-label="Foto des Inhabers im Kellner-Outfit mit Tablett und Sektgläsern"></div>
  <svg class="front-bands" viewBox="0 0 540 310" preserveAspectRatio="none" aria-hidden="true">
    <path d="M540,214 L390,214 C360,214 356,252 324,256 L0,302 L0,310 L540,310 Z" fill="#e8801e"/>
    <path d="M326,242 L0,288 L0,295 L322,249 Z" fill="#ffffff"/>
  </svg>
  <div class="edge-mark"></div>

  <div class="brand brand--small">
    <span class="brand__mark"></span>
    <span class="brand__name">velmora tandem</span>
  </div>
  <p class="tagline tagline--small">...weil jedes Fest gute Leute braucht!</p>

  <div class="identity">
    <p class="identity__name">JONAS HALLBERG</p>
    <p class="identity__role">INHABER</p>
  </div>

  <ul class="contacts">
    <li>01234 555 01 24 <svg viewBox="0 0 10 10"><path d="M2 1l2 2-1 1.5c.8 1.4 1.7 2.3 3 3L7.5 6l2 2-1.5 1.5C5 9 1 5 .5 2z"/></svg></li>
    <li>0150 555 08 63 <svg viewBox="0 0 10 10"><path d="M2 1l2 2-1 1.5c.8 1.4 1.7 2.3 3 3L7.5 6l2 2-1.5 1.5C5 9 1 5 .5 2z"/></svg></li>
    <li>info@velmora-tandem.de <svg viewBox="0 0 10 10"><rect x="1" y="2" width="8" height="6"/><path d="M1 2l4 3 4-3"/></svg></li>
    <li>www.velmora-tandem.de <svg viewBox="0 0 10 10"><circle cx="5" cy="5" r="4"/><path d="M1 5h8M5 1c-2 2.5-2 5.5 0 8M5 1c2 2.5 2 5.5 0 8"/></svg></li>
    <li>Lindenweg 14, 12345 Musterstadt <svg viewBox="0 0 10 10"><path d="M5 9.5C2.5 6.5 2 5 2 4a3 3 0 0 1 6 0c0 1-.5 2.5-3 5.5z" fill="#e8801e"/></svg></li>
  </ul>
</section>

<section class="card card--back" aria-label="Rückseite">
  <div class="brand brand--large">
    <span class="brand__mark"></span>
    <span class="brand__name">velmora tandem</span>
  </div>
  <p class="tagline tagline--large">...weil jedes Fest gute Leute braucht!</p>
  <p class="social"><span class="social__dot"></span>www.velmora-tandem.de/events</p>
</section>

</body>
</html>
```